Images and design ideas provided: Postcard size flier

2 sided postcard size flier to hand people on the street.

A FUN tax business needs a postcard size flier to hand people on the street. Not a typical serious, quiet, office so make the image fun!

Exact wording, logo and key images provided. You are free to add other images as you see fit (such as money).

Side 1: Use image of lady looking up (she should be looking at text provided).All spanish and english text provided. Logo in bottom right corner. Address at bottom of card.

Side 2: Image of lady holding money and pointing. Remove money and have her holding a sign/or some other creative way to have her looking at text. All spanish and english text provided. Logo in bottom right corner. Address at bottom of card.

Size: 4" x 6" horizontal or vertical is ok
Each side can be different and image/design does not have to be related.

Target Market(s)

Age 18-35

Industry/Entity Type

Accounting

Font styles to use
Sans Serif

Colors

Designer to choose colors to be used in the design.

Requirements
Must have
• Use text document provided. All text goes on both sides.
• Should be easy to read from a few feet away.
Nice to have
• Bright colors to attract attention of people walking by to grab flier/card. Images of money ok.
Should not have
• No images of calculators or typical accounting tax forms.

```html
<!DOCTYPE html>
<html lang="en">
<head>
<meta charset="utf-8">
<title>Bright Return Co. – Postcard Flier</title>
<link href="https://fonts.googleapis.com/css2?family=Anton&family=Oswald:wght@500;700&family=Patrick+Hand&display=swap" rel="stylesheet">
<style>
  :root {
    --backdrop: #e9d6b4;
    --white: #ffffff;
    --cream: #f8efc2;
    --sun-yellow: #f8d619;
    --olive-yellow: #c8ad12;
    --deep-gold: #b49a0c;
    --sky-blue: #4a8fe4;
    --line-blue: #3f86e0;
    --hot-red: #e8231c;
    --ink: #111111;
    --robe-green: #8a9a52;
    --robe-red: #a8202c;
    --hat-gold: #d8b54a;
  }
  * { box-sizing: border-box; margin: 0; padding: 0; }
  html, body { width: 1200px; height: 489px; overflow: hidden; }
  body { background: var(--backdrop); position: relative; font-family: "Oswald", sans-serif; }

  .card { position: absolute; top: 22px; height: 444px; overflow: hidden; }
  .card--front { left: 45px; width: 567px; background: var(--white); }
  .card--back { left: 632px; width: 533px; background: var(--cream); }

  .front-shapes, .back-shapes { position: absolute; inset: 0; }

  .headline {
    position: absolute; right: 108px; top: 8px;
    font-family: "Anton", sans-serif; font-size: 39px; color: var(--hot-red);
    letter-spacing: 0.5px; transform: rotate(-1.5deg);
  }
  .subline {
    position: absolute; right: 92px; top: 66px;
    font-family: "Oswald", sans-serif; font-weight: 500; font-size: 14px; color: var(--ink);
  }
  .spanish {
    position: absolute; left: 50px; top: 78px; width: 510px;
    transform: rotate(2.4deg); transform-origin: left top;
    color: var(--white); font-family: "Patrick Hand", sans-serif; text-align: center;
  }
  .spanish__main { font-size: 31px; line-height: 1.05; letter-spacing: 1px; }
  .spanish__sub { font-size: 18px; line-height: 1.2; letter-spacing: 0.5px; }

  .photo { position: absolute; }
  .photo--front {
    left: 0; top: 140px; width: 290px; height: 304px;
    background: linear-gradient(160deg, rgba(120,150,90,0.55), var(--robe-green) 55%, var(--robe-red));
    border-radius: 40px 40px 0 0;
  }
  .photo--back {
    left: 8px; top: 0; width: 440px; height: 345px;
    background: radial-gradient(ellipse at 35% 30%, var(--hat-gold), var(--robe-green) 60%, var(--robe-red));
    border-radius: 0 0 120px 40px;
  }

  .address {
    position: absolute; font-family: "Oswald", sans-serif; font-weight: 700;
    color: var(--ink); text-transform: uppercase; line-height: 1.25;
  }
  .address--front { left: 310px; top: 286px; font-size: 16px; }
  .address--back { left: 36px; top: 356px; font-size: 14px; }
  .phone { display: flex; align-items: center; gap: 6px; font-size: 1.15em; }
  .phone svg { width: 15px; height: 15px; }

  .brand {
    position: absolute; display: flex; align-items: center; gap: 10px;
    font-family: "Oswald", sans-serif; font-weight: 700; color: var(--hot-red);
    line-height: 1.05; text-transform: none;
  }
  .brand__dot { width: 30px; height: 30px; border-radius: 50%; background: var(--sky-blue); flex: none; }
  .brand--front { left: 245px; top: 378px; font-size: 22px; }
  .brand--back { left: 262px; top: 372px; font-size: 20px; }

  .sign {
    position: absolute; left: 293px; top: 48px; width: 216px; height: 126px;
    background: var(--sky-blue); border-radius: 12px;
    display: flex; align-items: center; justify-content: center; text-align: center;
    color: var(--white); font-family: "Oswald", sans-serif; font-weight: 700;
    font-size: 25px; line-height: 1.25; text-transform: uppercase;
  }
</style>
</head>
<body>

  <section class="card card--front">
    <svg class="front-shapes" viewBox="0 0 567 444" preserveAspectRatio="none" aria-hidden="true">
      <polygon points="0,150 567,172 567,444 0,444" fill="var(--sun-yellow)"/>
      <polygon points="0,150 380,165 567,300 567,444 0,444" fill="var(--olive-yellow)"/>
      <polygon points="380,165 567,172 567,300" fill="var(--deep-gold)" opacity="0.35"/>
      <polygon points="220,260 567,250 567,444 150,444" fill="var(--sun-yellow)"/>
      <polygon points="0,72 567,96 567,178 0,152" fill="var(--line-blue)"/>
    </svg>

    <div class="headline">GET $100 CASH NOW!</div>
    <div class="subline">WITH PAID TAX PREPARATION</div>
    <div class="spanish">
      <div class="spanish__main">RECIBA $100 EN EFECTIVO AHORA!</div>
      <div class="spanish__sub">CON LA PREPARA PAGADA DE SUS IMPUESTOS</div>
    </div>

    <div class="photo photo--front" role="img" aria-label="Photo of a smiling woman in a playful king costume looking up as dollar bills rain down"></div>

    <div class="address address--front">
      <div>275 Harbor Ave.</div>
      <div>Riverside, New York 10520</div>
      <div class="phone">
        <svg viewBox="0 0 16 16" aria-hidden="true"><circle cx="8" cy="8" r="7.2" fill="none" stroke="var(--ink)" stroke-width="1.4"/><path d="M5.3 4.2l1.5 1.6-.8 1.1c.5 1.1 1.2 1.9 2.3 2.4l1.1-.8 1.6 1.5-1 1.3C7.3 11 4.8 8.6 4.3 5.2z" fill="var(--ink)"/></svg>
        <span>(555) 240.0187</span>
      </div>
    </div>

    <div class="brand brand--front">
      <span class="brand__dot" aria-hidden="true"></span>
      <span>Bright<br>Return Co.</span>
    </div>
  </section>

  <section class="card card--back">
    <svg class="back-shapes" viewBox="0 0 533 444" preserveAspectRatio="none" aria-hidden="true">
      <path d="M0,330 C150,362 330,362 533,312 L533,444 L0,444 Z" fill="var(--sun-yellow)"/>
      <path d="M0,330 C150,362 330,362 533,312" fill="none" stroke="var(--line-blue)" stroke-width="5"/>
    </svg>

    <div class="photo photo--back" role="img" aria-label="Photo of a cheerful woman in a king costume and crown hat pointing at the sign she holds"></div>

    <div class="sign">Keep more of<br>your money!</div>

    <div class="address address--back">
      <div>275 Harbor Ave.</div>
      <div>Riverside, New York 10520</div>
      <div class="phone">
        <svg viewBox="0 0 16 16" aria-hidden="true"><circle cx="8" cy="8" r="7.2" fill="none" stroke="var(--ink)" stroke-width="1.4"/><path d="M5.3 4.2l1.5 1.6-.8 1.1c.5 1.1 1.2 1.9 2.3 2.4l1.1-.8 1.6 1.5-1 1.3C7.3 11 4.8 8.6 4.3 5.2z" fill="var(--ink)"/></svg>
        <span>(555) 240.0187</span>
      </div>
    </div>

    <div class="brand brand--back">
      <span class="brand__dot" aria-hidden="true"></span>
      <span>Bright<br>Return Co.</span>
    </div>
  </section>

</body>
</html>
```